LLC needs a business card design that emphasizes consulting and expert witness in upstream oil and g

I need a business card design for my company called Kelvora Consultative Service, LLC. My expertise is in oil and gas upstream operations management to optimize performance and also as an expert witness for law firms in oil and gas upstream operations litigation.
The final design should communicate knowledge and hands-on experience as well as trust. (Kelvora means rope or lasso. Perhaps "Kelvora" should be in the form of a rope.) I do not like the color green in any shade. My first preference would be some shade of blue.
Oil And Gas

```html
<!DOCTYPE html>
<html lang="en">
<head>
<meta charset="utf-8">
<title>Kelvora Consultative Service — Business Card</title>
<link href="https://fonts.googleapis.com/css2?family=PT+Sans:wght@400&family=Tinos:wght@400;700&display=swap" rel="stylesheet">
<style>
  :root {
    --stage: #b9b9bb;
    --stage-light: #d6d6d8;
    --brand-blue: #1f4fb0;
    --brand-blue-deep: #1a3f96;
    --brand-blue-light: #2c63c9;
    --ink-navy: #1d3c8c;
    --paper: #ffffff;
    --paper-shade: #f1f1f3;
    --silver-1: #e9e9ec;
    --silver-2: #9fa2a8;
    --text-light: #ffffff;
  }
  * { box-sizing: border-box; margin: 0; padding: 0; }
  html, body {
    width: 1200px; height: 900px; overflow: hidden;
    background: radial-gradient(ellipse at 50% 40%, var(--stage-light), var(--stage) 75%);
    font-family: "Tinos", "Times New Roman", serif;
  }
  .stage {
    width: 1200px; height: 900px;
    display: flex; align-items: center; justify-content: center; gap: 60px;
  }
  .card {
    width: 520px; height: 300px; border-radius: 22px; overflow: hidden;
    position: relative;
    box-shadow: 0 14px 30px rgba(0,0,0,.28);
  }
  /* Front */
  .card--front {
    background: linear-gradient(160deg, var(--brand-blue-light), var(--brand-blue) 55%, var(--brand-blue-deep));
    display: flex; align-items: center; justify-content: center;
  }
  .wordmark { display: flex; flex-direction: column; align-items: flex-end; }
  .wordmark__row { display: flex; align-items: center; gap: 14px; }
  .wordmark__dot { width: 34px; height: 34px; border-radius: 50%; background: var(--text-light); }
  .wordmark__name {
    font-family: "Tinos", "Times New Roman", serif; font-weight: 700;
    font-size: 64px; line-height: 1; color: var(--text-light);
  }
  .wordmark__tagline {
    font-family: "PT Sans", Arial, sans-serif; font-size: 20px;
    color: var(--text-light); margin-top: 4px;
  }
  /* Back */
  .card--back { background: var(--paper); }
  .card__top {
    height: 150px; display: flex; align-items: center; padding-left: 40px;
    background: linear-gradient(180deg, var(--paper), var(--paper-shade));
  }
  .card--back .wordmark__dot { background: var(--ink-navy); }
  .card--back .wordmark__name,
  .card--back .wordmark__tagline { color: var(--ink-navy); }
  .card__rule {
    height: 10px;
    background: linear-gradient(180deg, var(--silver-1), var(--silver-2));
  }
  .card__bottom {
    height: 140px; padding: 16px 30px;
    background: linear-gradient(180deg, var(--brand-blue-light), var(--brand-blue-deep));
  }
  .contact { list-style: none; color: var(--text-light); font-size: 17px; line-height: 24px; }
  .contact li { display: flex; align-items: flex-start; gap: 8px; }
  .contact svg { width: 18px; height: 18px; margin-top: 3px; flex: none; fill: var(--text-light); }
</style>
</head>
<body>
<main class="stage">
  <section class="card card--front" aria-label="Card front">
    <div class="wordmark">
      <div class="wordmark__row">
        <span class="wordmark__dot"></span>
        <span class="wordmark__name">Kelvora</span>
      </div>
      <span class="wordmark__tagline">Consultative Service</span>
    </div>
  </section>

  <section class="card card--back" aria-label="Card back">
    <div class="card__top">
      <div class="wordmark">
        <div class="wordmark__row">
          <span class="wordmark__dot"></span>
          <span class="wordmark__name">Kelvora</span>
        </div>
        <span class="wordmark__tagline">Consultative Service</span>
      </div>
    </div>
    <div class="card__rule"></div>
    <div class="card__bottom">
      <ul class="contact">
        <li>
          <svg viewBox="0 0 24 24" aria-hidden="true"><path d="M6.6 10.8a15 15 0 0 0 6.6 6.6l2.2-2.2c.3-.3.7-.4 1-.2 1.1.4 2.3.6 3.6.6.6 0 1 .4 1 1V20c0 .6-.4 1-1 1A17 17 0 0 1 3 4c0-.6.4-1 1-1h3.5c.6 0 1 .4 1 1 0 1.3.2 2.5.6 3.6.1.3 0 .7-.2 1z"/></svg>
          <span>555-214-0387</span>
        </li>
        <li>
          <svg viewBox="0 0 24 24" aria-hidden="true"><path d="M3 5h18v14H3z M4.5 6.5 12 12l7.5-5.5" stroke="#fff" stroke-width="0" /><path d="M3 5h18v14H3V5zm2 2v.3l7 5 7-5V7H5zm14 2.7-7 5-7-5V17h14V9.7z"/></svg>
          <span>info@kelvoraconsultative.com</span>
        </li>
        <li>
          <svg viewBox="0 0 24 24" aria-hidden="true"><path d="M12 2a10 10 0 1 0 0 20 10 10 0 0 0 0-20zm6.9 9h-3a15 15 0 0 0-1.3-6A8 8 0 0 1 18.9 11zM12 4c.9 1.3 1.7 3.8 1.9 7h-3.8C10.3 7.8 11.1 5.3 12 4zM9.4 5a15 15 0 0 0-1.3 6h-3A8 8 0 0 1 9.4 5zM5.1 13h3a15 15 0 0 0 1.3 6A8 8 0 0 1 5.1 13zM12 20c-.9-1.3-1.7-3.8-1.9-7h3.8c-.2 3.2-1 5.7-1.9 7zm2.6-1a15 15 0 0 0 1.3-6h3a8 8 0 0 1-4.3 6z"/></svg>
          <span>www.kelvoraconsultative.com</span>
        </li>
        <li>
          <svg viewBox="0 0 24 24" aria-hidden="true"><path d="M12 3 2 12h3v8h5v-5h4v5h5v-8h3z"/></svg>
          <span>4820 W. Marlow Road,<br>Tyler, Texas 75701</span>
        </li>
      </ul>
    </div>
  </section>
</main>
</body>
</html>
```